Tallyleaf Web Design

Create Website Design for Tallyleaf. Tallyleaf is online application for collaboration team work system (task list management). More concept design for this project please find attach file ("tallyleaf website concept.pdf") . But my concept is just describe minimal features not bind design

For tallyleaf logo, i had already attach files. But i had not decided what color i chose, so it's okay if you suggest logo color for your suitable website design.
Updates

Dear All Designer,

I like brisk carousel (http://quorvanlabs.example/brisk-carousel/),
may be your concept design can adjust with this concept.
but don't worry about script for brisk carousel, my team will be handle
You just make website design to suitable with brisk carousel

but if you had own website design concept are welcome

thanks

Target Market(s)

Business Company

Industry/Entity Type

Management

```html
<!DOCTYPE html>
<html lang="en">
<head>
<meta charset="utf-8">
<title>Tallyleaf – Online Collaboration Team Work</title>
<link rel="stylesheet" href="https://fonts.googleapis.com/css2?family=Montserrat:wght@400;500;600;700&family=Open+Sans:wght@400;700&display=swap">
<style>
  :root {
    --cream-top: #ffffff;
    --cream-bottom: #f1eedd;
    --rule-grey: #dedbd3;
    --dark-band: #2b2b2b;
    --lime: #c3dc4f;
    --leaf-green: #86bf2a;
    --phone-red: #b8131c;
    --text-grey: #555555;
    --nav-text: #333333;
    --nav-top: #ffffff;
    --nav-bottom: #dcdcdc;
    --login-blue: #3aaed6;
    --magenta: #c8116f;
    --panel-bg: #f3f3f3;
    --card-border: #e2e2e2;
    --footer-grey: #a9a9a9;
    --social-blue: #2f7fc1;
  }
  * { margin: 0; padding: 0; box-sizing: border-box; }
  html, body { width: 1200px; height: 883px; overflow: hidden; }
  body { position: relative; font-family: "Montserrat", sans-serif; background: var(--panel-bg); }

  .site-header {
    position: absolute; left: 0; top: 0; width: 1200px; height: 154px;
    background: linear-gradient(var(--cream-top), var(--cream-bottom));
    border-top: 5px solid var(--rule-grey);
  }
  .brand { position: absolute; left: 141px; top: 30px; display: flex; align-items: center; gap: 12px; }
  .brand-name { font-family: "Montserrat", sans-serif; font-weight: 600; font-size: 62px; color: var(--leaf-green); letter-spacing: -1px; line-height: 1; }
  .brand-dot { width: 26px; height: 26px; border-radius: 50%; background: var(--login-blue); margin-top: 8px; }

  .call-us { position: absolute; left: 868px; top: 38px; color: var(--text-grey); font-size: 19px; line-height: 1.2; }
  .call-us strong { display: block; color: var(--phone-red); font-weight: 700; font-size: 21px; letter-spacing: 0.5px; }

  .hero-band { position: absolute; left: 0; top: 154px; width: 1200px; height: 342px; background: var(--dark-band); }

  .main-nav {
    position: absolute; left: 141px; top: 126px; width: 919px; height: 41px; z-index: 2;
    background: linear-gradient(var(--nav-top), var(--nav-bottom));
    border: 1px solid #cfcfcf; border-radius: 4px; box-shadow: 0 2px 3px rgba(0,0,0,0.25);
    display: flex; align-items: center;
  }
  .main-nav a { color: var(--nav-text); text-decoration: none; font-size: 16px; font-weight: 500; height: 100%; display: flex; align-items: center; justify-content: center; border-right: 1px solid #c9c9c9; }
  .main-nav a.nav-home { width: 95px; }
  .main-nav a.nav-services { width: 121px; }
  .main-nav a.nav-products { width: 128px; }
  .main-nav a.nav-about { width: 128px; }
  .main-nav a.nav-contact { width: 120px; border-right: none; }
  .login-button {
    position: absolute; right: 5px; top: 5px; width: 96px; height: 30px; border-radius: 3px;
    background: var(--login-blue); color: #fff; font-size: 19px; font-weight: 600;
    display: flex; align-items: center; justify-content: center; gap: 6px;
  }

  .hero-slide { position: absolute; left: 140px; top: 188px; width: 563px; height: 290px;
    background: linear-gradient(180deg, #7b8a94 0%, #4d5a66 45%, #2f3944 100%); }
  .hero-title { position: absolute; left: 722px; top: 190px; color: var(--lime); font-size: 50px; font-weight: 500; line-height: 45px; letter-spacing: -0.5px; }
  .hero-text { position: absolute; left: 723px; top: 399px; width: 300px; color: #fff; font-family: "Open Sans", sans-serif; font-size: 14.5px; line-height: 18px; }

  .feature-card { position: absolute; top: 528px; width: 291px; height: 266px; background: #fff; border: 1px solid var(--card-border); border-radius: 5px; box-shadow: 0 0 4px rgba(0,0,0,0.06); }
  .feature-card.card-apps { left: 138px; }
  .feature-card.card-sync { left: 454px; }
  .feature-card.card-report { left: 770px; }
  .feature-image { position: absolute; left: 20px; top: 20px; width: 249px; height: 137px; }
  .card-apps .feature-image { background: linear-gradient(#f1f1f1, #d8d8d8); }
  .card-sync .feature-image { background: linear-gradient(90deg, #eaf6fa, #cbe9f3); }
  .card-report .feature-image { background: linear-gradient(135deg, #f2f2f2 0%, #e4e4e4 55%, #f0a640 75%, #5a6aa0 100%); }
  .feature-title { position: absolute; left: 17px; top: 173px; color: var(--magenta); font-size: 18px; font-weight: 500; }
  .feature-text { position: absolute; left: 17px; top: 208px; width: 260px; color: var(--text-grey); font-family: "Open Sans", sans-serif; font-size: 13px; line-height: 18px; }

  .site-footer { position: absolute; left: 0; top: 823px; width: 1200px; height: 60px; background: var(--dark-band); }
  .footer-links { position: absolute; left: 140px; top: 12px; color: #fff; font-family: "Open Sans", sans-serif; font-size: 11px; font-weight: 700; }
  .footer-links a { color: #fff; text-decoration: none; }
  .footer-links span { margin: 0 4px; }
  .copyright { position: absolute; left: 140px; top: 33px; color: var(--footer-grey); font-family: "Open Sans", sans-serif; font-size: 11px; }
  .follow-us { position: absolute; left: 991px; top: 7px; color: #fff; font-family: "Open Sans", sans-serif; font-size: 12px; }
  .social-links { position: absolute; left: 980px; top: 27px; display: flex; gap: 7px; }
  .social-links span { width: 23px; height: 23px; border-radius: 3px; background: var(--social-blue); }
</style>
</head>
<body>
  <header class="site-header">
    <div class="brand"><span class="brand-name">tallyleaf</span><span class="brand-dot"></span></div>
    <div class="call-us">Call us today<strong>(12) 555 018 4471</strong></div>
  </header>

  <div class="hero-band"></div>

  <nav class="main-nav">
    <a class="nav-home" href="#">Home</a>
    <a class="nav-services" href="#">Services</a>
    <a class="nav-products" href="#">Products</a>
    <a class="nav-about" href="#">About Us</a>
    <a class="nav-contact" href="#">Contact</a>
    <span class="login-button">
      <svg width="14" height="18" viewBox="0 0 14 18" aria-hidden="true">
        <path d="M3.5 8V5.5a3.5 3.5 0 0 1 7 0V8" fill="none" stroke="#fff" stroke-width="2"/>
        <rect x="1" y="8" width="12" height="9" rx="1.5" fill="#fff"/>
      </svg>Login</span>
  </nav>

  <div class="hero-slide" role="img" aria-label="Photo of a smiling business team standing together in an office"></div>
  <h1 class="hero-title">Customize<br>Online<br>Collaboration<br>Team Work</h1>
  <p class="hero-text">Aenean sollicitudin, lorem quis bibendum auctor, nisi elit consequat ipsum, nec sagittis sem nibh id elit.</p>

  <section class="feature-card card-apps">
    <div class="feature-image" role="img" aria-label="Laptop showing the task management application"></div>
    <h2 class="feature-title">Customize Application</h2>
    <p class="feature-text">Proin gravida nibh vel velit auctor aliquet. Aenean sollicitudin, lorem quis.</p>
  </section>
  <section class="feature-card card-sync">
    <div class="feature-image" role="img" aria-label="Smartphone showing the synchronized application"></div>
    <h2 class="feature-title">Synchronize All Device</h2>
    <p class="feature-text">Proin gravida nibh vel velit auctor aliquet. Aenean sollicitudin, lorem quis.</p>
  </section>
  <section class="feature-card card-report">
    <div class="feature-image" role="img" aria-label="Printed sales report with colourful bar chart"></div>
    <h2 class="feature-title">Report</h2>
    <p class="feature-text">Proin gravida nibh vel velit auctor aliquet. Aenean sollicitudin, lorem quis.</p>
  </section>

  <footer class="site-footer">
    <div class="footer-links"><a href="#">Home</a><span>\</span><a href="#">Services</a><span>\</span><a href="#">Products</a><span>\</span><a href="#">About Us</a><span>\</span><a href="#">Contact</a></div>
    <div class="copyright">Copyright © 2013 Harborline Build Co. All Rights Reserved.</div>
    <div class="follow-us">Follow us</div>
    <div class="social-links"><span></span><span></span><span></span></div>
  </footer>
</body>
</html>
```